Mattress sale flyer front and back

FLYER SIZE!! front and back!
4.25" X 5.5"
or
10.7cm X 13.9 cm

This flyer needs to show the prices
twin.....$99
full.......$159
queen...$199
king....$299

the phone number........(786)413-9072
the address ..........24315 sw 142st miami fl 33157
if possible a map would be appreciated

possible brands to include.......Dravo, Quillard, brook & vantle, plumnight

ATTACHED IS OUR OLD FLYER WITH OUTDATED INFORMATION, I WOULD LIKE SOMETHING SIMILAR. JUST ADD A LITTLE PRICE LIST AND A MAP

***FRONT AND BACK PLEASE****

```html
<!DOCTYPE html>
<html lang="en">
<head>
<meta charset="utf-8">
<title>Palmetto Mattress Outlet – Sale Flyer</title>
<link rel="stylesheet" href="https://fonts.googleapis.com/css2?family=Arimo:ital,wght@0,400;0,700;1,700&display=swap">
<style>
  :root {
    --sale-red: #b7302e;
    --price-red: #c40d0d;
    --ink: #111111;
    --logo-grey: #555555;
    --paper: #ffffff;
    --brand-blue: #1f4e8c;
    --map-base: #e9e6df;
    --map-light: #f4f2ec;
    --mattress-light: #fbf8f1;
    --mattress-shade: #e4ddcd;
  }
  * { margin: 0; padding: 0; box-sizing: border-box; }
  html, body { width: 848px; height: 1200px; overflow: hidden; background: var(--paper); }
  body { font-family: "Arimo", Arial, sans-serif; }

  .flyer { position: relative; width: 848px; height: 1200px; overflow: hidden; background: var(--paper); }

  .sale-banner { position: absolute; left: 0; top: 0; width: 848px; height: 285px; }
  .sale-banner text { font-family: "Arimo", Arial, sans-serif; fill: var(--paper); }

  .store-name {
    position: absolute; left: 300px; top: 280px; width: 470px;
    text-align: center; font-size: 40px; font-weight: 400;
    color: var(--logo-grey); letter-spacing: 1px;
  }
  .store-name .mark {
    display: inline-block; width: 16px; height: 16px; margin-right: 12px;
    background: var(--logo-grey); vertical-align: middle; position: relative; top: -3px;
  }

  .mattress-photo {
    position: absolute; left: 0; top: 435px; width: 350px; height: 370px;
    background: linear-gradient(180deg, var(--mattress-light) 0%, var(--mattress-shade) 100%);
  }

  .price-list { position: absolute; left: 406px; top: 450px; list-style: none; }
  .price-list li {
    font-size: 68px; line-height: 82px; color: var(--price-red); white-space: nowrap;
  }

  .rule { position: absolute; left: 0; width: 848px; height: 3px; background: var(--price-red); }
  .rule-top { top: 814px; }
  .rule-bottom { top: 923px; }

  .brand-strip { position: absolute; left: 0; top: 820px; width: 848px; height: 100px; }
  .brand {
    position: absolute; top: 30px; font-size: 22px; font-weight: 700;
    color: var(--brand-blue); white-space: nowrap;
  }
  .brand-quillard { left: 10px; }
  .brand-dravo { left: 172px; }
  .brand-corvane { left: 270px; }
  .brand-brook { left: 384px; }
  .brand-plumnight { left: 560px; }
  .brand-more {
    position: absolute; left: 683px; top: 20px; width: 165px;
    font-size: 20px; line-height: 26px; color: var(--ink); text-align: right;
  }
  .brand-more em { font-weight: 700; }

  .location-map {
    position: absolute; left: 0; top: 929px; width: 342px; height: 271px;
    background: linear-gradient(135deg, var(--map-light) 0%, var(--map-base) 100%);
  }

  .contact { position: absolute; left: 373px; top: 938px; }
  .contact-label { font-size: 23px; color: var(--price-red); line-height: 30px; }
  .contact-address { font-style: normal; font-size: 24px; line-height: 31px; color: var(--ink); margin-top: 6px; }
  .contact-call { position: absolute; left: 368px; top: 1110px; font-size: 23px; color: var(--price-red); }
  .contact-phone { position: absolute; left: 432px; top: 1142px; font-size: 23px; color: var(--price-red); }

  .page-curl {
    position: absolute; right: 0; bottom: 0; width: 52px; height: 76px;
    background: linear-gradient(135deg, #ffffff 0%, #cfcfcf 60%, #9a9a9a 100%);
  }
</style>
</head>
<body>
<main class="flyer">
  <svg class="sale-banner" viewBox="0 0 595 200" aria-hidden="false" role="img" aria-label="Sale banner">
    <defs>
      <clipPath id="banner-wave">
        <path d="M0 0 H595 V100 C540 92 480 90 420 108 C350 128 270 150 170 146 C100 143 45 140 0 150 Z"/>
      </clipPath>
    </defs>
    <path d="M0 0 H595 V100 C540 92 480 90 420 108 C350 128 270 150 170 146 C100 143 45 140 0 150 Z" fill="var(--sale-red)"/>
    <g clip-path="url(#banner-wave)">
      <text x="-2" y="38" font-size="44">Sale</text>
      <text x="28" y="132" font-size="96">Sale</text>
      <text x="184" y="60" font-size="44">Sale</text>
      <text x="266" y="92" font-size="72">Sale</text>
      <text x="404" y="76" font-size="34">Sale</text>
      <text x="198" y="138" font-size="30">Sale</text>
      <text x="330" y="132" font-size="28">Sale</text>
      <text x="440" y="124" font-size="34">Sale</text>
      <text x="488" y="108" font-size="76">Sale</text>
      <text x="553" y="24" font-size="40">Sa</text>
    </g>
  </svg>

  <div class="store-name"><span class="mark"></span>Palmetto Mattress Outlet</div>

  <div class="mattress-photo" role="img" aria-label="Stack of four white pillow-top mattresses in twin, full, queen and king sizes"></div>

  <ul class="price-list">
    <li>Twin.....$99</li>
    <li>Full.......$159</li>
    <li>Queen...$199</li>
    <li>King....$299</li>
  </ul>

  <div class="rule rule-top"></div>
  <section class="brand-strip">
    <span class="brand brand-quillard">Quillard</span>
    <span class="brand brand-dravo">Dravo</span>
    <span class="brand brand-corvane">Corvane</span>
    <span class="brand brand-brook">brook &amp; vantle</span>
    <span class="brand brand-plumnight">plumnight</span>
    <p class="brand-more">and many more other <em>GREAT</em> brands!</p>
  </section>
  <div class="rule rule-bottom"></div>

  <div class="location-map" role="img" aria-label="Street map showing the store location on SW 142nd St, Miami"></div>

  <section class="contact">
    <p class="contact-label">Our location:</p>
    <address class="contact-address">24315 SW 142st<br>Miami, FL<br>33157</address>
  </section>
  <p class="contact-call">Call us at:</p>
  <p class="contact-phone">(786)413-9072</p>

  <div class="page-curl" role="img" aria-label="Turned page corner"></div>
</main>
</body>
</html>
```